Makeup Artist looking to redesign business card

I'm a makeup artist relocating from Sydney to the Tweed Heads Area. I will be providing makeup services (primarily in bridal/wedding, events) in the Tweed Heads, Gold Coast and Byron Bay areas. I have attached 2 photos to use on the front OR back of the card. I can't decide which photo will work best, so I have provided both for you to decide. I'm open to the idea of a logo creation, or just the business name. Business name is;
Harriet Rose Calloway Makeup Artist
or
Harriet Calloway Makeup Artist
I will need a space for ABN, mobile number, email address and website address.
I'm open to the photo being either colour or B&W.
Font and background colour could be B&W or another colour, again I'm looking for something different and creative, which is why I'm posting this ad.
I do like the idea of the photo being panoramic, so the veil material continues off to the side.
I'm excited to see what people come up with!!!
Target Market(s)
ladies
Industry/Entity Type
Business
Contact Information for Business Card
or

```html
<!DOCTYPE html>
<html lang="en">
<head>
<meta charset="utf-8">
<title>Harriet Calloway – Makeup Artist Business Card</title>
<link rel="stylesheet" href="https://fonts.googleapis.com/css2?family=Great+Vibes&family=Cinzel:wght@400&family=Open+Sans:wght@400&display=swap">
<style>
  :root {
    --stage: #000000;
    --plum: #a3298e;
    --rose: #e84b8f;
    --silver: #a7a5a8;
    --ink-light: #ffffff;
    --photo-light: #f1ecea;
    --photo-warm: #d8b39c;
  }
  * { box-sizing: border-box; margin: 0; padding: 0; }
  html, body {
    width: 999px; height: 1200px; overflow: hidden;
    background: var(--stage);
  }
  .stage { position: relative; width: 999px; height: 1200px; }
  .card {
    position: absolute; left: 53px; width: 901px; height: 515px;
    background: var(--plum); overflow: hidden; color: var(--ink-light);
  }
  .card--front { top: 86px; }
  .card--back { top: 628px; }

  .brand { position: absolute; text-align: right; }
  .brand__name {
    font-family: "Great Vibes", cursive; font-weight: 400;
    line-height: 1; white-space: nowrap;
  }
  .brand__role {
    font-family: "Cinzel", serif; letter-spacing: 0.5px;
    line-height: 1; white-space: nowrap;
  }
  .card--front .brand { left: 52px; top: 30px; }
  .card--front .brand__name { font-size: 64px; }
  .card--front .brand__role { font-size: 29px; margin-top: 2px; }

  .card--back .brand { left: 50%; top: 190px; transform: translateX(-50%); }
  .card--back .brand__name { font-size: 82px; }
  .card--back .brand__role { font-size: 38px; margin-top: 2px; }

  .address {
    position: absolute; left: 58px; top: 294px;
    font-family: "Open Sans", sans-serif; font-size: 22px; line-height: 33px;
  }
  .contacts {
    position: absolute; left: 58px; top: 382px; list-style: none;
    font-family: "Open Sans", sans-serif; font-size: 22px;
  }
  .contacts li { display: flex; align-items: center; height: 34px; }
  .contacts svg { width: 24px; height: 24px; margin-right: 24px; fill: none; stroke: var(--ink-light); stroke-width: 1.8; }
  .contacts .solid { fill: var(--ink-light); stroke: none; }

  .portrait { position: absolute; left: 0; top: 0; width: 901px; height: 515px; }
</style>
</head>
<body>
<main class="stage">
  <section class="card card--front">
    <svg class="portrait" viewBox="0 0 901 515">
      <defs>
        <clipPath id="portrait-clip"><circle cx="868" cy="257.5" r="338"/></clipPath>
        <linearGradient id="portrait-tone" x1="0" y1="0" x2="0.4" y2="1">
          <stop offset="0" stop-color="var(--photo-light)"/>
          <stop offset="0.45" stop-color="var(--photo-warm)"/>
          <stop offset="1" stop-color="var(--photo-light)"/>
        </linearGradient>
      </defs>
      <circle cx="868" cy="257.5" r="346" fill="var(--silver)"/>
      <circle cx="868" cy="257.5" r="338" fill="var(--rose)"/>
      <g clip-path="url(#portrait-clip)">
        <circle cx="905" cy="330" r="375" fill="url(#portrait-tone)" role="img" aria-label="Portrait photo of the makeup artist wrapped in white veil fabric"/>
      </g>
    </svg>

    <div class="brand">
      <h1 class="brand__name">Harriet Calloway</h1>
      <p class="brand__role">Makeup Artist</p>
    </div>

    <p class="address">suit # 00, Lorem ipsum<br>Lorem Lorem ipsum</p>

    <ul class="contacts">
      <li>
        <svg viewBox="0 0 24 24" aria-hidden="true">
          <path class="solid" d="M6 3l3 4-2 2c1 3 4 6 7 7l2-2 4 3-2 3c-8 0-15-7-15-15z"/>
          <path d="M14 5a5 5 0 0 1 5 5M14 1.5a8.5 8.5 0 0 1 8.5 8.5"/>
        </svg>
        000-000-0000
      </li>
      <li>
        <svg viewBox="0 0 24 24" aria-hidden="true">
          <path class="solid" d="M2 10l10-7 10 7v11H2z"/>
          <path d="M3 11l9 6 9-6" stroke="var(--plum)"/>
        </svg>
        abcde@harrietcalloway.com
      </li>
      <li>
        <svg viewBox="0 0 24 24" aria-hidden="true">
          <circle cx="12" cy="12" r="9.5"/>
          <ellipse cx="12" cy="12" rx="4" ry="9.5"/>
          <path d="M2.5 12h19M4 7h16M4 17h16"/>
        </svg>
        www.harrietcalloway.com
      </li>
    </ul>
  </section>

  <section class="card card--back">
    <div class="brand">
      <h2 class="brand__name">Harriet Calloway</h2>
      <p class="brand__role">Makeup Artist</p>
    </div>
  </section>
</main>
</body>
</html>
```